Corporate Template

Looking for a set of corporate slides to be made which contain multiple different slides and orientations. Looking for at least 8 to 10 different master pages plus a Coversheet and closeout page. Incorporating a color palate similar to our logo coloring is preferred.
I have attached a logo.
I like the clever pixel yard designs best so far. They seem to fit what I'm looking for in terms of visual appearance.
Reason: I'm trying to allow time for a couple new designers to incorporate some changes I requested to their existing designs.

```html
<!DOCTYPE html>
<html lang="en">
<head>
<meta charset="utf-8">
<title>Corvane Health – Corporate Slide Masters</title>
<link href="https://fonts.googleapis.com/css2?family=Carlito:wght@400;700&display=swap" rel="stylesheet">
<style>
:root{
  --brand-blue:#3a6cb5;
  --accent:#8b2a83;
  --ink:#222;
  --ink-soft:#555;
  --gray-1:#e6e6e6;
  --gray-2:#d2d4d6;
  --gray-3:#9a9a9a;
  --gray-4:#6d6d6d;
  --frame:#8c8c8c;
  --paper:#fff;
}
*{box-sizing:border-box;margin:0;padding:0}
html,body{width:1200px;height:720px;overflow:hidden;background:var(--paper)}
body{font-family:"Carlito",sans-serif;color:var(--ink)}
.deck{position:absolute;left:26px;top:33px;display:grid;grid-template-columns:repeat(4,276px);grid-template-rows:repeat(4,155px);column-gap:15px;row-gap:11px}
.slide{position:relative;border:1px solid var(--frame);background:var(--paper);overflow:hidden}
.slide--blue{background:var(--brand-blue);color:#fff}
.footer{position:absolute;left:8px;bottom:5px;font-size:3.2px;color:var(--gray-3);white-space:nowrap}
.slide--blue .footer{color:#dfe7f4}
.corner-mark{position:absolute;right:8px;bottom:5px;color:var(--brand-blue);font-size:5px;font-weight:700}
.slide--blue .corner-mark{color:#fff}
.slide-title{font-weight:700;font-size:10.5px;position:absolute;left:10px;top:8px}
.slide-sub{font-size:7px;position:absolute;left:10px;top:22px}
.heading{color:var(--brand-blue);font-weight:700;font-size:6.5px;line-height:1.15}
.body{font-size:6px;margin-top:3px}
.bullets{list-style:none;font-size:5px;line-height:1.3}
.bullets li{position:relative;padding-left:6px;margin-top:1px}
.bullets li::before{content:"•";position:absolute;left:1px}
.bullets .l2{padding-left:11px}
.bullets .l2::before{content:"–";left:5px}
.bullets .l3{padding-left:16px}
.bullets .l3::before{left:11px}
.content{position:absolute;left:10px;top:35px}
.note{position:absolute;left:10px;top:38px;font-size:5px}
/* cover */
.cover-name{position:absolute;left:0;right:0;top:30px;text-align:center;color:var(--brand-blue);font-size:19px;font-weight:400;line-height:1}
.slide--blue .cover-name{color:#fff}
.cover-title{position:absolute;left:0;right:0;top:78px;text-align:center;font-weight:700;font-size:15px;line-height:1.05;color:var(--ink-soft)}
.cover-sub{position:absolute;left:0;right:0;top:116px;text-align:center;font-size:5.5px;color:var(--gray-4);line-height:1.7}
.cover-sub .speaker{font-size:7px}
.slide--blue .cover-title,.slide--blue .cover-sub{color:#fff}
/* photo slides */
.photo{position:absolute;inset:0}
.photo--clinic{background:linear-gradient(100deg,#f2f1ee 0%,#d8d4cd 40%,#f6f6f5 60%,#c9c4bd 100%)}
.photo--chart{background:radial-gradient(circle at 75% 35%,#d9c6b4 0%,#b89a82 35%,#8e7865 70%,#efe9e1 100%)}
.photo-title{position:absolute;left:10px;top:62px;font-size:13.5px;font-weight:700;line-height:1.05;color:var(--ink)}
.photo-sub{position:absolute;left:10px;top:101px;font-size:5.5px}
.photo-title.right{left:140px;top:85px}
.photo-sub.right{left:140px;top:122px}
.figure{position:absolute;left:148px;top:34px;width:114px;height:95px;background:linear-gradient(180deg,#e3efe1,#cfe3cf);border:1px solid #b6c9b4}
/* quote / thanks */
.quote{position:absolute;left:10px;top:8px;font-size:13.5px;font-weight:700;line-height:1.15}
.quote-by{position:absolute;left:10px;top:97px;font-size:5.5px;line-height:1.3}
.thanks{position:absolute;left:10px;top:8px;font-size:13px;font-weight:700}
/* two column */
.col{position:absolute;top:35px;width:120px}
/* org charts */
.org-head{position:absolute;left:10px;top:46px;background:var(--brand-blue);color:#fff;font-size:4.6px;font-weight:700;padding:1.5px 3px;width:78px;line-height:1.2}
.org-row{position:absolute;left:10px;display:flex;gap:2px}
.org-box{background:var(--gray-4);color:#fff;font-size:3.8px;font-weight:700;padding:1px 2px;width:39px;height:9px;line-height:1.1}
.org-cell{background:var(--gray-1);font-size:3.6px;padding:1px 2px;width:39px;height:9px;line-height:1.1}
.org-cell.alt{background:var(--gray-2)}
.tree-item{font-size:3.6px;line-height:1.15;width:39px;padding-left:6px;height:12px}
/* flow */
.flow{position:absolute;left:10px;top:50px;display:flex;gap:3px}
.step{width:47px}
.step svg{display:block}
.step ul{margin-top:4px}
/* table */
.grid{position:absolute;left:10px;top:44px;border-collapse:separate;border-spacing:1px;font-size:4px}
.grid td,.grid th{height:8px;padding:0 3px;text-align:left}
.grid th{background:var(--brand-blue);color:#fff;width:32px}
.grid th.blank{background:none;width:108px}
.grid tr:nth-child(even) td{background:var(--gray-1)}
.grid tr:nth-child(odd) td{background:var(--gray-2)}
.grid .hl{color:var(--brand-blue)}
/* charts */
.legend{position:absolute;font-size:4.5px;line-height:1.5;white-space:nowrap}
.swatch{display:inline-block;width:4px;height:4px;margin-right:2px;vertical-align:middle}
</style>
</head>
<body>
<main class="deck">

  <section class="slide">
    <p class="cover-name">Corvane Health</p>
    <h1 class="cover-title">Title<br>(46 pt. Calibri bold)</h1>
    <p class="cover-sub">Subtitle (18 pt. Calibri)<br><span class="speaker">Speaker's name / Month day, 2013</span></p>
    <p class="footer">© 2013 Corvane Health | 100 Sample Road, Suite 1, Austin</p>
  </section>

  <section class="slide">
    <div class="photo photo--clinic" role="img" aria-label="Photo of a doctor in a white coat holding a tablet"></div>
    <h2 class="photo-title">Click to edit master<br>title style</h2>
    <p class="photo-sub">Click to edit master subtitle style</p>
    <p class="footer">© 2013 Corvane Health | 100 Sample Road, Suite 1, Austin</p>
    <span class="corner-mark">Corvane Health</span>
  </section>

  <section class="slide">
    <h2 class="slide-title">Title (28 pt. Calibri bold)</h2>
    <p class="slide-sub">Subtitle (18 pt. Calibri)</p>
    <div class="content" style="width:130px">
      <p class="heading">Heading (18 pt. Calibri bold<br>CVH blue)</p>
      <p class="body">Body copy (16 pt. Calibri)</p>
      <ul class="bullets">
        <li>Put your first-level bullet here.<br>(14 pt. Calibri)</li>
        <li class="l2">Put your second-level bullet here.<br>(14 pt. Calibri)</li>
        <li class="l3">Put your third-level of copy here.<br>(14 pt. Calibri)</li>
      </ul>
    </div>
    <div class="figure" role="img" aria-label="Brain wave recording chart on green grid paper"></div>
    <p class="footer">© 2013 Corvane Health | 100 Sample Road, Suite 1, Austin</p>
  </section>

  <section class="slide">
    <h2 class="slide-title">Title (28 pt. Calibri bold)</h2>
    <p class="slide-sub">Subtitle (18 pt. Calibri)</p>
    <div class="content" style="width:255px">
      <p class="heading">Heading (18 pt. Calibri bold CVH blue)</p>
      <p class="body">Body copy (16 pt. Calibri)</p>
      <ul class="bullets">
        <li>Put your first-level bullet here. Try to keep bullet lists simple. (14 pt. Calibri)</li>
        <li class="l2">Put your second-level bullet here. Use no more than you need to explain your point. (14 pt. Calibri)</li>
        <li class="l3">Put your third-level of copy here. Use no more than you need to explain your point. (14 pt. Calibri)</li>
      </ul>
    </div>
    <p class="footer">© 2013 Corvane Health | 100 Sample Road, Suite 1, Austin</p>
  </section>

  <section class="slide slide--blue">
    <p class="cover-name">Corvane Health</p>
    <h1 class="cover-title">Title<br>(46 pt. Calibri bold)</h1>
    <p class="cover-sub">Subtitle (18 pt. Calibri)<br><span class="speaker">Speaker's name / Month day, 2013</span></p>
    <p class="footer">© 2013 Corvane Health | 100 Sample Road, Suite 1, Austin</p>
  </section>

  <section class="slide">
    <div class="photo photo--chart" role="img" aria-label="Photo of a clinician reviewing a printed heart trace"></div>
    <h2 class="photo-title right">Click to edit master<br>title style</h2>
    <p class="photo-sub right">Click to edit master subtitle style</p>
    <p class="footer">© 2013 Corvane Health | 100 Sample Road, Suite 1, Austin</p>
    <span class="corner-mark">Corvane Health</span>
  </section>

  <section class="slide slide--blue">
    <h2 class="quote">“Insert quote here”<br>(40 pt. Calibri bold)</h2>
    <p class="quote-by">Quoted person's name, title and company<br>(18 pt. Calibri)</p>
    <p class="footer">© 2013 Corvane Health | 100 Sample Road, Suite 1, Austin</p>
  </section>

  <section class="slide">
    <h2 class="slide-title">Title (28 pt. Calibri bold)</h2>
    <p class="slide-sub">Subtitle (18 pt. Calibri)</p>
    <div class="col" style="left:10px">
      <p class="heading">Heading (18 pt. Calibri bold<br>CVH blue)</p>
      <p class="body">Body copy (16 pt. Calibri)</p>
      <ul class="bullets">
        <li>Put your first-level bullet here.<br>(14 pt. Calibri)</li>
        <li class="l2">Put your second-level bullet here.<br>(14 pt. Calibri)</li>
        <li class="l3">Put your third-level of copy here.<br>(14 pt. Calibri)</li>
      </ul>
    </div>
    <div class="col" style="left:138px">
      <p class="heading">Heading (18 pt. Calibri bold<br>CVH blue)</p>
      <p class="body">Body copy (16 pt. Calibri)</p>
      <ul class="bullets">
        <li>Put your first-level bullet here.<br>(14 pt. Calibri)</li>
        <li class="l2">Put your second-level bullet here.<br>(14 pt. Calibri)</li>
        <li class="l3">Put your third-level of copy here.<br>(14 pt. Calibri)</li>
      </ul>
    </div>
    <p class="footer">© 2013 Corvane Health | 100 Sample Road, Suite 1, Austin</p>
  </section>

  <section class="slide">
    <h2 class="slide-title">Organization chart style (expanded)</h2>
    <p class="note">Box size and quantity may vary, but colors must be maintained.</p>
    <div class="org-head">Insert Name<br>Title goes here (12 pt. Calibri bold)</div>
    <svg style="position:absolute;left:0;top:0" width="276" height="155" aria-hidden="true">
      <path d="M38 60 V64 M30 64 H235 M30 64 V67 M71 64 V67 M112 64 V67 M153 64 V67 M194 64 V67 M235 64 V67" stroke="#888" stroke-width=".6" fill="none"/>
    </svg>
    <div class="org-row" style="top:67px">
      <div class="org-box">This level is all the same color</div>
      <div class="org-box">11 pt. Calibri bold</div><div class="org-box">11 pt. Calibri bold</div><div class="org-box">11 pt. Calibri bold</div><div class="org-box">11 pt. Calibri bold</div><div class="org-box">11 pt. Calibri bold</div>
    </div>
    <div class="org-row" style="top:78px"><div class="org-cell">Name<br>Title</div><div class="org-cell">11 pt.<br>Calibri</div><div class="org-cell">11 pt.<br>Calibri</div><div class="org-cell">11 pt.<br>Calibri</div><div class="org-cell">11 pt.<br>Calibri</div><div class="org-cell">11 pt.<br>Calibri</div></div>
    <div class="org-row" style="top:89px"><div class="org-cell alt">Name<br>Title</div><div class="org-cell alt">11 pt.<br>Calibri</div><div class="org-cell alt">11 pt.<br>Calibri</div><div class="org-cell alt">11 pt.<br>Calibri</div><div class="org-cell alt">11 pt.<br>Calibri</div><div class="org-cell alt">11 pt.<br>Calibri</div></div>
    <div class="org-row" style="top:100px"><div class="org-cell">Name<br>Title</div><div class="org-cell">11 pt.<br>Calibri</div><div class="org-cell">11 pt.<br>Calibri</div><div class="org-cell">11 pt.<br>Calibri</div><div class="org-cell">11 pt.<br>Calibri</div><div class="org-cell">11 pt.<br>Calibri</div></div>
    <div class="org-row" style="top:111px"><div class="org-cell alt">Name<br>Title</div><div class="org-cell alt">11 pt.<br>Calibri</div><div class="org-cell alt">11 pt.<br>Calibri</div><div class="org-cell alt">11 pt.<br>Calibri</div><div class="org-cell alt">11 pt.<br>Calibri</div><div class="org-cell alt">11 pt.<br>Calibri</div></div>
    <div class="org-row" style="top:122px"><div class="org-cell">Name<br>Title</div><div class="org-cell">11 pt.<br>Calibri</div><div class="org-cell">11 pt.<br>Calibri</div><div class="org-cell">11 pt.<br>Calibri</div><div class="org-cell">11 pt.<br>Calibri</div><div class="org-cell">11 pt.<br>Calibri</div></div>
    <p class="footer">© 2013 Corvane Health | 100 Sample Road, Suite 1, Austin</p>
  </section>

  <section class="slide">
    <h2 class="slide-title">Flow chart style</h2>
    <p class="note">Box size and quantity may vary, but colors must be maintained.</p>
    <div class="flow">
      <div class="step"><svg width="47" height="12"><polygon points="0,0 41,0 47,6 41,12 0,12" fill="#3a6cb5"/><text x="3" y="5" font-size="3.8" fill="#fff" font-weight="700">12 pt. bold</text><text x="3" y="9.5" font-size="3.8" fill="#fff" font-weight="700">Calibri</text></svg>
        <ul class="bullets" style="font-size:4px"><li>A percentage of or solid black may be used</li><li>11 pt. Calibri</li></ul></div>
      <div class="step"><svg width="47" height="12"><polygon points="0,0 41,0 47,6 41,12 0,12 6,6" fill="#8a8a8a"/><text x="8" y="5" font-size="3.8" fill="#fff" font-weight="700">12 pt. bold</text><text x="8" y="9.5" font-size="3.8" fill="#fff" font-weight="700">Calibri</text></svg>
        <ul class="bullets" style="font-size:4px"><li>A percentage of or solid black may be used</li><li>11 pt. Calibri</li></ul></div>
      <div class="step"><svg width="47" height="12"><polygon points="0,0 41,0 47,6 41,12 0,12 6,6" fill="#8a8a8a"/><text x="8" y="5" font-size="3.8" fill="#fff" font-weight="700">12 pt. bold</text><text x="8" y="9.5" font-size="3.8" fill="#fff" font-weight="700">Calibri</text></svg>
        <ul class="bullets" style="font-size:4px"><li>A percentage of or solid black may be used</li><li>11 pt. Calibri</li></ul></div>
      <div class="step"><svg width="47" height="12"><polygon points="0,0 41,0 47,6 41,12 0,12 6,6" fill="#8a8a8a"/><text x="8" y="5" font-size="3.8" fill="#fff" font-weight="700">12 pt. bold</text><text x="8" y="9.5" font-size="3.8" fill="#fff" font-weight="700">Calibri</text></svg>
        <ul class="bullets" style="font-size:4px"><li>A percentage of or solid black may be used</li><li>11 pt. Calibri</li></ul></div>
      <div class="step"><svg width="47" height="12"><polygon points="0,0 41,0 47,6 41,12 0,12 6,6" fill="#8a8a8a"/><text x="8" y="5" font-size="3.8" fill="#fff" font-weight="700">12 pt. bold</text><text x="8" y="9.5" font-size="3.8" fill="#fff" font-weight="700">Calibri</text></svg>
        <ul class="bullets" style="font-size:4px"><li>A percentage of or solid black may be used</li><li>11 pt. Calibri</li></ul></div>
    </div>
    <p class="footer">© 2013 Corvane Health | 100 Sample Road, Suite 1, Austin</p>
  </section>

  <section class="slide">
    <h2 class="slide-title">Pie chart sample</h2>
    <div class="content" style="top:26px;width:115px">
      <p style="font-size:5.5px;line-height:1.25">Segments may vary, but only use CVH blue, one accent color and the permitted values of black.</p>
      <ul class="bullets" style="margin-top:2px"><li>All other copy is black.</li><li>Bullets are 14 pt. Calibri.</li><li>Pie segment percentages are 14 pt. Calibri.</li><li>Pie legend is 14 pt. Calibri.</li></ul>
    </div>
    <svg style="position:absolute;left:118px;top:28px" width="108" height="100" aria-label="Pie chart">
      <g transform="translate(54,52)">
        <path d="M0 0 L0 -40 A40 40 0 1 1 -21.4 33.8 Z" fill="#3a6cb5"/>
        <path d="M0 0 L-21.4 33.8 A40 40 0 0 1 -36.2 -17 Z" fill="#8b2a83"/>
        <path d="M0 0 L-36.2 -17 A40 40 0 0 1 -19.3 -35 Z" fill="#d6d6d6"/>
        <path d="M0 0 L-19.3 -35 A40 40 0 0 1 0 -40 Z" fill="#8f8f8f"/>
      </g>
      <g font-size="4.5" fill="#333"><text x="46" y="8">8%</text><text x="6" y="24">10%</text><text x="20" y="96">23%</text><text x="97" y="68">59%</text></g>
    </svg>
    <div class="legend" style="left:228px;top:46px">
      <div><span class="swatch" style="background:var(--brand-blue)"></span>CVH Blue</div>
      <div><span class="swatch" style="background:var(--accent)"></span>Accent color</div>
      <div><span class="swatch" style="background:#d6d6d6"></span>Value of black</div>
      <div><span class="swatch" style="background:#8f8f8f"></span>Value of black</div>
    </div>
    <p class="footer">© 2013 Corvane Health | 100 Sample Road, Suite 1, Austin</p>
  </section>

  <section class="slide">
    <h2 class="slide-title">Bar chart sample</h2>
    <p class="note" style="top:26px">Data may vary, but only use CVH blue, one accent color and the permitted values of black.</p>
    <svg style="position:absolute;left:10px;top:38px" width="256" height="90" aria-label="Bar chart">
      <g stroke="#ddd" stroke-width=".4">
        <line x1="12" y1="4" x2="250" y2="4"/><line x1="12" y1="20" x2="250" y2="20"/><line x1="12" y1="36" x2="250" y2="36"/><line x1="12" y1="52" x2="250" y2="52"/><line x1="12" y1="68" x2="250" y2="68"/>
      </g>
      <line x1="12" y1="84" x2="250" y2="84" stroke="#999" stroke-width=".5"/>
      <g font-size="4.5" fill="#555"><text x="5" y="86">0</text><text x="5" y="70">1</text><text x="5" y="54">2</text><text x="5" y="38">3</text><text x="5" y="22">4</text><text x="5" y="6">5</text></g>
      <g fill="#3a6cb5"><rect x="24" y="61.6" width="8" height="22.4"/><rect x="72" y="39.2" width="8" height="44.8"/><rect x="120" y="18.4" width="8" height="65.6"/><rect x="168" y="7.2" width="8" height="76.8"/><rect x="216" y="39.2" width="8" height="44.8"/></g>
      <g fill="#8b2a83"><rect x="33" y="47.2" width="8" height="36.8"/><rect x="81" y="55.2" width="8" height="28.8"/><rect x="129" y="31.2" width="8" height="52.8"/><rect x="177" y="24.8" width="8" height="59.2"/><rect x="225" y="16.8" width="8" height="67.2"/></g>
      <g fill="#c8c8c8"><rect x="42" y="24.8" width="8" height="59.2"/><rect x="90" y="50.4" width="8" height="33.6"/><rect x="138" y="71.2" width="8" height="12.8"/><rect x="186" y="16.8" width="8" height="67.2"/><rect x="234" y="28" width="8" height="56"/></g>
      <g font-size="4.5" fill="#555" text-anchor="middle"><text x="37" y="90">2009</text><text x="85" y="90">2010</text><text x="133" y="90">2011</text><text x="181" y="90">2012</text><text x="229" y="90">2013</text></g>
    </svg>
    <div class="legend" style="left:58px;top:131px;display:flex;gap:14px">
      <span><span class="swatch" style="background:var(--brand-blue)"></span>CVH Blue (14 pt. Calibri)</span>
      <span><span class="swatch" style="background:var(--accent)"></span>Accent color</span>
      <span><span class="swatch" style="background:#c8c8c8"></span>Value of black</span>
    </div>
    <p class="footer">© 2013 Corvane Health | 100 Sample Road, Suite 1, Austin</p>
  </section>

  <section class="slide">
    <h2 class="slide-title">Table style</h2>
    <p class="note" style="top:30px">Columns and rows may be added, but colors must be maintained.</p>
    <table class="grid">
      <tr><th class="blank"></th><th>Heading</th><th>Heading</th><th>Heading</th><th>Heading</th></tr>
      <tr><td>12 pt. Calibri</td><td>Content</td><td>Content</td><td>Content</td><td>Content</td></tr>
      <tr><td>Content</td><td>Content</td><td>Content</td><td>Content</td><td>Content</td></tr>
      <tr><td>Content</td><td>Content</td><td>Content</td><td>Content</td><td>Content</td></tr>
      <tr><td>Content</td><td>Content</td><td>Content</td><td>Content</td><td>Content</td></tr>
      <tr><td class="hl">12 pt. Calibri bold CVH blue</td><td class="hl">Content</td><td class="hl">Content</td><td class="hl">Content</td><td class="hl">Content</td></tr>
      <tr><td>Content</td><td>Content</td><td>Content</td><td>Content</td><td>Content</td></tr>
    </table>
    <p class="footer">© 2013 Corvane Health | 100 Sample Road, Suite 1, Austin</p>
  </section>

  <section class="slide">
    <h2 class="slide-title">Organisation chart style (condensed)</h2>
    <p class="note" style="top:28px">Box size and quantity may vary, but colors must be maintained.</p>
    <div class="org-head" style="top:38px">Insert Name<br>Title goes here (12 pt. Calibri bold)</div>
    <svg style="position:absolute;left:0;top:0" width="276" height="155" aria-hidden="true">
      <path d="M38 50 V54 M30 54 H235 M30 54 V57 M81 54 V57 M132 54 V57 M183 54 V57 M234 54 V57" stroke="#888" stroke-width=".6" fill="none"/>
      <g stroke="#888" stroke-width=".5" fill="none">
        <path d="M14 66 V124 M14 72 H18 M14 87 H18 M14 101 H18 M14 116 H18"/>
        <path d="M65 66 V124 M65 72 H69 M65 87 H69 M65 101 H69 M65 116 H69"/>
        <path d="M116 66 V124 M116 72 H120 M116 87 H120 M116 101 H120 M116 116 H120"/>
        <path d="M167 66 V124 M167 72 H171 M167 87 H171 M167 101 H171 M167 116 H171"/>
        <path d="M218 66 V124 M218 72 H222 M218 87 H222 M218 101 H222 M218 116 H222"/>
      </g>
    </svg>
    <div class="org-row" style="top:57px;gap:6px;left:10px">
      <div class="org-box" style="width:45px">This level is all the same color</div>
      <div class="org-box" style="width:45px">11 pt. Calibri bold</div><div class="org-box" style="width:45px">11 pt. Calibri bold</div><div class="org-box" style="width:45px">11 pt. Calibri bold</div><div class="org-box" style="width:45px">11 pt. Calibri bold</div>
    </div>
    <div class="org-row" style="top:69px;gap:12px;left:12px">
      <div><div class="tree-item">Name<br>Title</div><div class="tree-item" style="margin-top:3px">11 pt.<br>Calibri</div><div class="tree-item" style="margin-top:2px">11 pt.<br>Calibri</div><div class="tree-item" style="margin-top:2px">11 pt.<br>Calibri</div></div>
      <div><div class="tree-item">Name<br>Title</div><div class="tree-item" style="margin-top:3px">11 pt.<br>Calibri</div><div class="tree-item" style="margin-top:2px">11 pt.<br>Calibri</div><div class="tree-item" style="margin-top:2px">11 pt.<br>Calibri</div></div>
      <div><div class="tree-item">Name<br>Title</div><div class="tree-item" style="margin-top:3px">11 pt.<br>Calibri</div><div class="tree-item" style="margin-top:2px">11 pt.<br>Calibri</div><div class="tree-item" style="margin-top:2px">11 pt.<br>Calibri</div></div>
      <div><div class="tree-item">Name<br>Title</div><div class="tree-item" style="margin-top:3px">11 pt.<br>Calibri</div><div class="tree-item" style="margin-top:2px">11 pt.<br>Calibri</div><div class="tree-item" style="margin-top:2px">11 pt.<br>Calibri</div></div>
      <div><div class="tree-item">Name<br>Title</div><div class="tree-item" style="margin-top:3px">11 pt.<br>Calibri</div><div class="tree-item" style="margin-top:2px">11 pt.<br>Calibri</div><div class="tree-item" style="margin-top:2px">11 pt.<br>Calibri</div></div>
    </div>
    <p class="footer">© 2013 Corvane Health | 100 Sample Road, Suite 1, Austin</p>
  </section>

  <section class="slide">
    <h2 class="slide-title">Title (28 pt. Calibri bold)</h2>
    <p class="slide-sub">Subtitle (18 pt. Calibri)</p>
    <div class="content" style="width:130px">
      <p class="heading">Heading (18 pt. Calibri bold<br>CVH blue)</p>
      <p class="body">Body copy (16 pt. Calibri)</p>
      <ul class="bullets">
        <li>Put your first-level bullet here.<br>(14 pt. Calibri)</li>
        <li class="l2">Put your second-level bullet here.<br>(14 pt. Calibri)</li>
        <li class="l3">Put your third-level of copy here.<br>(14 pt. Calibri)</li>
      </ul>
    </div>
    <div class="figure" role="img" aria-label="Brain wave recording chart on green grid paper"></div>
    <p class="footer">© 2013 Corvane Health | 100 Sample Road, Suite 1, Austin</p>
  </section>

  <section class="slide slide--blue">
    <h2 class="thanks">Thank you</h2>
    <p class="footer">© 2013 Corvane Health | 100 Sample Road, Suite 1, Austin</p>
  </section>

</main>
</body>
</html>
```